Looking for a contemporary business card design with our logo

would like to consider a embossing look although I'm not married to the idea. We are a custom jeweler that needs a look that represents old world craftsmanship with a modern twist that's why we went with a more modern shield type of logo that can be stamped inside our rings.
It could be two sided or one we are more after a look the pops and is trendy and creative. (WE ARE NOT LOOKING FOR A COOKIE CUTTER LAYOUT)
We have attached the image and will be using the logo with harwick studio wording in the format that it's in unless you see a better way of doing it.
If the logo needs a twist we are O.K. with suggestions as well.
This card should scream "Quality" from a high end studio.
Harwick Studio
4186 Maplecrest Rd. Unit B-2
Ravenmoor, WY 80317
www.harwickstudio-example.com
lu@harwickstudio-example.com
Should speak quality craftsmanship

```html
<!DOCTYPE html>
<html lang="en">
<head>
<meta charset="utf-8">
<title>Harwick Studio — Business Card</title>
<link rel="stylesheet" href="https://fonts.googleapis.com/css2?family=Open+Sans:wght@400;600&display=swap">
<style>
  :root {
    --page-bg: #e9e7e4;
    --card-bg: #1b1b1b;
    --card-edge: #111111;
    --silver-light: #f2f2f2;
    --silver-mid: #b9b9b9;
    --silver-dark: #7d7d7d;
    --mark-grey: #a9a9a9;
    --text-light: #f0f0f0;
    --text-dark: #2a2a2a;
  }
  * { box-sizing: border-box; margin: 0; padding: 0; }
  html, body {
    width: 1200px; height: 1000px; overflow: hidden;
    background: var(--page-bg);
    font-family: "Open Sans", Arial, sans-serif;
  }
  .canvas { position: relative; width: 1200px; height: 1000px; }

  .card {
    position: absolute; left: 265px; width: 665px; height: 393px;
    background: var(--card-edge);
    padding: 10px;
    box-shadow: 0 6px 18px rgba(0,0,0,0.35);
  }
  .card--front { top: 75px; }
  .card--back { top: 535px; }

  .card__frame {
    width: 100%; height: 100%;
    padding: 4px;
    background: linear-gradient(90deg, var(--silver-dark), var(--silver-light) 30%, var(--silver-mid) 55%, var(--silver-light) 80%, var(--silver-dark));
  }
  .card__face {
    position: relative; width: 100%; height: 100%;
    background: radial-gradient(ellipse at 50% 45%, #242424, var(--card-bg) 70%);
  }

  .mark {
    position: absolute;
    display: flex; flex-direction: column; align-items: center;
    color: var(--mark-grey);
    font-weight: 600;
    letter-spacing: 4px;
    line-height: 1;
  }
  .mark__word { font-size: 38px; white-space: nowrap; }
  .mark__square {
    width: 74px; height: 74px; margin: 18px 0;
    background: var(--mark-grey);
  }
  .card--front .mark { left: 48px; top: 80px; width: 240px; }
  .card--back .mark { left: 0; right: 0; top: 60px; }
  .card--back .mark__word { font-size: 40px; }
  .card--back .mark__square { width: 80px; height: 80px; }

  .contact {
    position: absolute; left: 362px; top: 110px;
    color: var(--text-light);
    white-space: nowrap;
  }
  .contact__name { font-size: 24px; margin-bottom: 8px; }
  .contact__line { font-size: 16px; line-height: 25px; }
  .contact__links { margin-top: 14px; }
  .contact__link { display: flex; align-items: center; gap: 7px; font-size: 15px; line-height: 27px; }
  .contact__icon { width: 15px; height: 13px; flex: none; }

  .web-tab {
    position: absolute; left: 180px; bottom: -14px;
    width: 270px; height: 36px;
    display: flex; align-items: center; justify-content: center;
    background: linear-gradient(90deg, var(--silver-mid), var(--silver-light) 45%, var(--silver-mid) 75%, var(--silver-dark));
    color: var(--text-dark);
    font-size: 14px;
    white-space: nowrap;
  }
</style>
</head>
<body>
<main class="canvas">

  <section class="card card--front" aria-label="Card front">
    <div class="card__frame">
      <div class="card__face">
        <div class="mark">
          <span class="mark__word">HARWICK</span>
          <span class="mark__square"></span>
          <span class="mark__word">STUDIO</span>
        </div>
        <div class="contact">
          <p class="contact__name">Harwick Studio</p>
          <p class="contact__line">4186 Maplecrest Rd. Unit B-2</p>
          <p class="contact__line">Ravenmoor, WY 80317</p>
          <div class="contact__links">
            <p class="contact__link">
              <svg class="contact__icon" viewBox="0 0 15 13" aria-hidden="true"><rect x="1" y="2" width="13" height="9" fill="#f0f0f0"/><path d="M1 2 L7.5 7.5 L14 2" fill="none" stroke="#1b1b1b" stroke-width="1.3"/></svg>
              lu@harwickstudio-example.com
            </p>
            <p class="contact__link">
              <svg class="contact__icon" viewBox="0 0 15 13" aria-hidden="true"><rect x="1.5" y="1.5" width="12" height="8" fill="none" stroke="#f0f0f0" stroke-width="1.4"/><rect x="5" y="11" width="5" height="1.5" fill="#f0f0f0"/></svg>
              www.harwickstudio-example.com
            </p>
          </div>
        </div>
      </div>
    </div>
  </section>

  <section class="card card--back" aria-label="Card back">
    <div class="card__frame">
      <div class="card__face">
        <div class="mark">
          <span class="mark__word">HARWICK</span>
          <span class="mark__square"></span>
          <span class="mark__word">STUDIO</span>
        </div>
        <div class="web-tab">www.harwickstudio-example.com</div>
      </div>
    </div>
  </section>

</main>
</body>
</html>
```